Design a styled business card for an intimacy and attachment psychologist

I am a Psychologist providing online therapy to patients across the United States. My work is interpersonal and emotion-focused, with an emphasis on the client-therapist relationship. My primary areas of work are very personal, including sexuality and gender, abuse and trauma, and grief and loss. My target audience will be adults of all ages 18+.
My business card should convey a warm and inviting feeling of professionalism that is also casual and comfortable.
The front should be fairly simple and professional, consisting of:
- My name, Dr. Rosalind Petrakis
- My title, Licensed Psycholigist
- My logo
On either the front or the back, my contact information should be listed:
- ros@drrospetrakis.example
- 555.014.7788
- drrospetrakis.example
On the rear, I would like a description of the areas that I specialize in. This can be formatted in any way that appears stylistically interesting.
Individual and Couples
Relationships and Infidelity
Sexual Health & Aging
Gender Identity & Sexual Orientation
Abuse and Trauma
Sexual Compulsivity & Addiction
Sexual Dysfunction
Target Market(s)
My target audience will be adults of all ages 18+.
Industry/Entity Type
Psychology
Contact Information for Business Card
The front should be fairly simple and professional, consisting of: - My name, Dr. Rosalind Petrakis - My title, Licensed Psycholigist - My logo On either the front or the back, my contact information should be listed: - ros@drrospetrakis.example - 555.014.7788 - drrospetrakis.example On the rear, I would like a description of the areas that I specialize in. This can be formatted in any way that appears stylistically interesting. Individual and Couples Relationships and Infidelity Sexual Health & Aging Gender Identity & Sexual Orientation Abuse and Trauma Sexual Compulsivity & Addiction Sexual Dysfunction
- Follow brand guide

```html
<!DOCTYPE html>
<html lang="en">
<head>
<meta charset="utf-8">
<title>Dr. Rosalind Petrakis – Business Card</title>
<link rel="stylesheet" href="https://fonts.googleapis.com/css2?family=Arimo:wght@400;700&display=swap">
<style>
  :root {
    --backdrop: #2b2b2d;
    --card: #ffffff;
    --navy: #262443;
    --accent-red: #e5383b;
    --mark-teal: #5fcfb4;
    --ink-soft: #3a3856;
  }
  * { box-sizing: border-box; margin: 0; padding: 0; }
  html, body {
    width: 1200px; height: 779px; overflow: hidden;
    background: var(--backdrop);
    font-family: "Arimo", Arial, sans-serif;
    color: var(--navy);
  }
  .stage { position: relative; width: 1200px; height: 779px; }
  .card {
    position: absolute;
    width: 540px; height: 308px;
    background: var(--card);
    border-bottom: 3px solid var(--accent-red);
    border-left: 2px solid var(--accent-red);
    box-shadow: 0 14px 30px rgba(0,0,0,.45);
  }
  .card--back { left: 70px; top: 70px; }
  .card--front { left: 590px; top: 400px; }

  /* logo lockup */
  .mark-circle {
    width: 74px; height: 74px; border-radius: 50%;
    background: var(--mark-teal);
    border: 4px solid var(--navy);
    flex: none;
  }
  .wordmark {
    font-weight: 700; color: var(--navy);
    text-transform: uppercase; line-height: 1.02;
    letter-spacing: .5px;
  }
  .wordmark .wordmark__small { font-size: 15px; display: block; }
  .wordmark .wordmark__large { font-size: 27px; display: block; }

  /* back card */
  .specialties {
    position: absolute; left: 56px; top: 78px;
    list-style: none;
    font-size: 13px; line-height: 21px; color: var(--ink-soft);
  }
  .specialties li { position: relative; padding-left: 16px; }
  .specialties li::before {
    content: ""; position: absolute; left: 0; top: 8px;
    width: 5px; height: 5px; border-radius: 50%; background: var(--navy);
  }
  .back-logo {
    position: absolute; right: 50px; top: 60px;
    display: flex; flex-direction: column; align-items: center; gap: 14px;
  }
  .back-logo .wordmark { text-align: left; }

  /* front card */
  .front-logo {
    position: absolute; left: 130px; top: 50px;
    display: flex; align-items: center; gap: 18px;
  }
  .front-logo .mark-circle { width: 82px; height: 82px; }
  .identity {
    position: absolute; left: 60px; top: 198px; text-align: right; width: 250px;
  }
  .identity__name { font-size: 21px; font-weight: 700; color: var(--navy); }
  .identity__title { font-size: 15px; color: var(--accent-red); margin-top: 3px; }
  .divider {
    position: absolute; left: 330px; top: 186px;
    width: 1px; height: 74px; background: var(--navy);
  }
  .contact {
    position: absolute; left: 348px; top: 190px;
    list-style: none; font-size: 13px; line-height: 22px; color: var(--navy);
  }
  .contact li { display: flex; align-items: center; gap: 8px; }
  .contact svg { width: 12px; height: 12px; fill: var(--navy); flex: none; }
</style>
</head>
<body>
<main class="stage">

  <section class="card card--back" aria-label="Card back: areas of specialty">
    <ul class="specialties">
      <li>Stylistically interesting</li>
      <li>Individual and Couples</li>
      <li>Relationships and Infidelity</li>
      <li>Sexual Health &amp; Aging</li>
      <li>Gender Identity &amp; Sexual Orientation</li>
      <li>Abuse and Trauma</li>
      <li>Sexual Compulsivity &amp; Addiction</li>
      <li>Sexual Dysfunction</li>
    </ul>
    <div class="back-logo">
      <div class="mark-circle"></div>
      <div class="wordmark">
        <span class="wordmark__small">Dr.</span>
        <span class="wordmark__large">Rosalind</span>
        <span class="wordmark__large">Petrakis</span>
      </div>
    </div>
  </section>

  <section class="card card--front" aria-label="Card front: name and contact">
    <div class="front-logo">
      <div class="mark-circle"></div>
      <div class="wordmark">
        <span class="wordmark__small">Dr.</span>
        <span class="wordmark__large">Rosalind</span>
        <span class="wordmark__large">Petrakis</span>
      </div>
    </div>

    <div class="identity">
      <p class="identity__name">Dr. Rosalind Petrakis</p>
      <p class="identity__title">Licensed Psycholigist</p>
    </div>

    <div class="divider"></div>

    <ul class="contact">
      <li>
        <svg viewBox="0 0 24 24" aria-hidden="true"><path d="M6.6 10.8a15 15 0 0 0 6.6 6.6l2.2-2.2a1 1 0 0 1 1-.25 11.4 11.4 0 0 0 3.6.57 1 1 0 0 1 1 1V20a1 1 0 0 1-1 1A17 17 0 0 1 3 4a1 1 0 0 1 1-1h3.5a1 1 0 0 1 1 1c0 1.25.2 2.45.57 3.6a1 1 0 0 1-.25 1z"/></svg>
        555.014.7788
      </li>
      <li>
        <svg viewBox="0 0 24 24" aria-hidden="true"><path d="M2 5h20v14H2z M4 7v.5l8 5 8-5V7l-8 5z" fill-rule="evenodd"/></svg>
        ros@drrospetrakis.example
      </li>
      <li>
        <svg viewBox="0 0 24 24" aria-hidden="true"><circle cx="12" cy="12" r="10"/></svg>
        www.drrospetrakis.example
      </li>
    </ul>
  </section>

</main>
</body>
</html>
```